Brindle Logistics Business Card Design

We are a trucking and warehousing company. We run freight in the US manly from the Pacific NW to TX and back up the the PNW. We also do warehousing where we store, move, and distribute freight. Looking for a clean and modern design of business card. We would like to look rich and elegant. Attached is our logo.

Industry/Entity Type

Trucking Company

Contact Information for Business Card

Looking for a clean and modern design of business card. We would like to look rich and elegant.

Font styles to use
Sans Serif

Colors

Designer to choose colors to be used in the design.

Requirements
Must have
• logo but it should not dominate the card
Should not have
• logo should not dominate the card

```html
<!DOCTYPE html>
<html lang="en">
<head>
<meta charset="utf-8">
<title>Brindle Logistics Business Card</title>
<link rel="stylesheet" href="https://fonts.googleapis.com/css2?family=Open+Sans:wght@400;500;600&display=swap">
<style>
  :root {
    --stage-light: #f4f4f4;
    --stage-dark: #8e8e8e;
    --card-dark: #2a2a2b;
    --card-dark-2: #4a4a4c;
    --panel-grey: #48484a;
    --frame-grey: #5a595b;
    --white: #ffffff;
    --ink: #3b3b3d;
    --accent-blue: #1d7fc4;
    --gold-1: #7b4f1d;
    --gold-2: #b8894a;
    --gold-3: #f0dca8;
    --gold-4: #9a6a2e;
  }
  * { margin: 0; padding: 0; box-sizing: border-box; }
  html, body { width: 1200px; height: 1000px; overflow: hidden; }
  body {
    position: relative;
    font-family: "Open Sans", Arial, sans-serif;
    background: radial-gradient(ellipse 620px 520px at 600px 505px, var(--stage-light) 0%, #c4c4c4 45%, var(--stage-dark) 100%);
  }
  .card {
    position: absolute;
    left: 258px;
    width: 662px;
    height: 405px;
    overflow: hidden;
  }
  .card svg.shapes { position: absolute; inset: 0; }
  .card-front { top: 78px; }
  .card-back { top: 540px; height: 405px; background: var(--white); }

  .front-texture {
    position: absolute; inset: 0;
    background: radial-gradient(ellipse 300px 220px at 270px 110px, #8c8a8c 0%, #4a494b 45%, var(--card-dark) 100%);
  }

  .wordmark {
    position: absolute;
    display: flex;
    align-items: center;
    color: var(--ink);
    font-weight: 600;
    line-height: 1;
  }
  .wordmark .dot {
    border-radius: 50%;
    background: var(--accent-blue);
    flex: none;
  }
  .wordmark .name { letter-spacing: 0.02em; }
  .wordmark .sub { display: block; letter-spacing: 0.04em; margin-top: 4px; }

  .front-mark { left: 210px; top: 178px; gap: 12px; }
  .front-mark .dot { width: 50px; height: 50px; }
  .front-mark .name { font-size: 34px; }
  .front-mark .sub { font-size: 15px; }

  .back-mark { left: 40px; top: 180px; gap: 9px; }
  .back-mark .dot { width: 38px; height: 38px; }
  .back-mark .name { font-size: 26px; }
  .back-mark .sub { font-size: 11.5px; }

  .contact-panel {
    position: absolute;
    left: 332px; top: 0; width: 330px; height: 405px;
    background: linear-gradient(160deg, #545456 0%, var(--panel-grey) 50%, #3e3e40 100%);
  }
  .holder-name {
    position: absolute; left: 381px; top: 60px;
    color: var(--white); font-size: 19px; font-weight: 400; letter-spacing: 0.02em;
  }
  .holder-role {
    position: absolute; left: 381px; top: 92px;
    color: #e6e6e6; font-size: 9.5px; letter-spacing: 0.12em;
  }
  .role-rule {
    position: absolute; left: 505px; top: 97px; width: 67px; height: 1px;
    background: var(--accent-blue);
  }
  .contact-list { list-style: none; }
  .contact-item {
    position: absolute; left: 331px;
    display: flex; align-items: center;
    height: 46px;
  }
  .contact-item svg { width: 50px; height: 46px; flex: none; }
  .contact-item span {
    margin-left: 12px;
    color: var(--white); font-size: 10.5px; letter-spacing: 0.1em;
  }
</style>
</head>
<body>

<section class="card card-front" aria-label="Card front">
  <div class="front-texture" role="img" aria-label="Dark woven texture background"></div>
  <svg class="shapes" width="662" height="405" viewBox="0 0 662 405" aria-hidden="true">
    <defs>
      <linearGradient id="goldBand" x1="0" x2="1" y1="0" y2="0">
        <stop offset="0" stop-color="#8a5a22"/>
        <stop offset="0.12" stop-color="#d8b676"/>
        <stop offset="0.3" stop-color="#a0702f"/>
        <stop offset="0.48" stop-color="#c0914e"/>
        <stop offset="0.6" stop-color="#7b4f1d"/>
        <stop offset="0.76" stop-color="#f0dca8"/>
        <stop offset="0.88" stop-color="#9a6a2e"/>
        <stop offset="1" stop-color="#7b4f1d"/>
      </linearGradient>
      <linearGradient id="frameGrey" x1="0" x2="1">
        <stop offset="0" stop-color="#3a393b"/>
        <stop offset="0.5" stop-color="#c9c4c4"/>
        <stop offset="1" stop-color="#3a393b"/>
      </linearGradient>
    </defs>
    <path class="gold-band" fill="url(#goldBand)" d="M17 0 H645 C632 0 640 42 612 50 H50 C22 42 30 0 17 0 Z"/>
    <path class="gold-band" fill="url(#goldBand)" d="M17 405 H645 C632 405 640 363 612 355 H50 C22 363 30 405 17 405 Z"/>
    <path class="logo-frame" fill="url(#frameGrey)" stroke="url(#frameGrey)" stroke-width="14" stroke-linejoin="round"
          d="M206 111 H445 L477 162 V245 L445 296 H206 L174 245 V162 Z"/>
    <path class="logo-plate" fill="#ffffff" stroke="#ffffff" stroke-width="16" stroke-linejoin="round"
          d="M218 127 H433 L461 169 V237 L433 279 H218 L190 237 V169 Z"/>
  </svg>
  <div class="wordmark front-mark">
    <span class="dot"></span>
    <div><span class="name">BRINDLE</span><span class="sub">LOGISTICS, LLC</span></div>
  </div>
</section>

<section class="card card-back" aria-label="Card back">
  <div class="contact-panel" role="img" aria-label="Grey textured contact panel"></div>
  <svg class="shapes" width="662" height="405" viewBox="0 0 662 405" aria-hidden="true">
    <defs>
      <linearGradient id="goldTab" x1="0" x2="0" y1="0" y2="1">
        <stop offset="0" stop-color="#8a5a22"/>
        <stop offset="0.25" stop-color="#f0dca8"/>
        <stop offset="0.45" stop-color="#b8894a"/>
        <stop offset="0.75" stop-color="#7b4f1d"/>
        <stop offset="1" stop-color="#c49552"/>
      </linearGradient>
    </defs>
    <path class="gold-tab" fill="url(#goldTab)"
          d="M0 121 H262 Q279 121 288 136 L307 190 Q311 202 307 214 L288 269 Q279 284 262 284 H0 Z"/>
  </svg>
  <div class="wordmark back-mark">
    <span class="dot"></span>
    <div><span class="name">BRINDLE</span><span class="sub">LOGISTICS, LLC</span></div>
  </div>

  <p class="holder-name">DALE HARPER</p>
  <p class="holder-role">PROJECT MANAGER</p>
  <div class="role-rule"></div>

  <svg width="0" height="0" style="position:absolute" aria-hidden="true">
    <defs>
      <linearGradient id="goldChip" x1="0" x2="0" y1="0" y2="1">
        <stop offset="0" stop-color="#8a5a22"/>
        <stop offset="0.3" stop-color="#e6cc92"/>
        <stop offset="0.6" stop-color="#a87a3a"/>
        <stop offset="1" stop-color="#7b4f1d"/>
      </linearGradient>
    </defs>
  </svg>

  <ul class="contact-list">
    <li class="contact-item" style="top:127px">
      <svg viewBox="0 0 50 46" aria-hidden="true">
        <path fill="url(#goldChip)" d="M0 0 H38 L49 23 L38 46 H0 Z"/>
        <g fill="none" stroke="#fff" stroke-width="1.6">
          <circle cx="20" cy="23" r="10"/>
          <ellipse cx="20" cy="23" rx="4.5" ry="10"/>
          <line x1="10" y1="23" x2="30" y2="23"/>
          <path d="M12 17 H28 M12 29 H28"/>
        </g>
      </svg>
      <span>WWW.YOURBRAND.COM</span>
    </li>
    <li class="contact-item" style="top:182px">
      <svg viewBox="0 0 50 46" aria-hidden="true">
        <path fill="url(#goldChip)" d="M0 0 H38 L49 23 L38 46 H0 Z"/>
        <path fill="#fff" d="M20 11 C14 11 11 15 11 19.5 C11 26 20 35 20 35 C20 35 29 26 29 19.5 C29 15 26 11 20 11 Z"/>
        <circle cx="20" cy="19.5" r="3.5" fill="#a87a3a"/>
      </svg>
      <span>LONDON, MAIN STREET, 12.C</span>
    </li>
    <li class="contact-item" style="top:236px">
      <svg viewBox="0 0 50 46" aria-hidden="true">
        <path fill="url(#goldChip)" d="M0 0 H38 L49 23 L38 46 H0 Z"/>
        <rect x="9" y="15" width="22" height="15" fill="#fff"/>
        <path d="M9 15 L20 24 L31 15 M9 30 L17 22 M31 30 L23 22" fill="none" stroke="#a87a3a" stroke-width="1.3"/>
      </svg>
      <span>EXAMPLE@COMPANY.COM</span>
    </li>
    <li class="contact-item" style="top:292px">
      <svg viewBox="0 0 50 46" aria-hidden="true">
        <path fill="url(#goldChip)" d="M0 0 H38 L49 23 L38 46 H0 Z"/>
        <path fill="#fff" d="M14 12 L18 11 L21 18 L18 20 C19 24 22 27 25 29 L27 26 L33 29 L32 33 C30 35 27 35 24 33 C18 30 13 24 12 18 C11.5 15 12 13 14 12 Z"/>
      </svg>
      <span>+011289 555 017</span>
    </li>
  </ul>
</section>

</body>
</html>
```